Wedding images design with personal names added

We have a big restaurant venue for weddings.  We wish to project onto the wall of our wedding venue , a very stylish, attractive and colourful pattern, graphic, pictures or design , with  the name of the bride and the groom in the middle .   So that the venue will be more unusual and welcoming and the wedding will be more memorable.
There 2 walls in our restaurant venue.  one wall is 9.8 meter high  x 18.5  meter wide .   Another wall is 2.5 meter high x 23.2 meter wide.

```html
<!DOCTYPE html>
<html lang="en">
<head>
<meta charset="utf-8">
<title>Wedding Welcome Projection Signs</title>
<link rel="stylesheet" href="https://fonts.googleapis.com/css2?family=Dancing+Script:wght@600;700&family=Cinzel:wght@400&family=Libre+Baskerville:wght@700&display=swap">
<style>
  :root {
    --backdrop: #e4e4e5;
    --frame-dark: #3b3b3c;
    --marble-light: #f7f6f3;
    --marble-mid: #ece8e1;
    --marble-vein: #d9c7a6;
    --gold-dark: #6e5327;
    --gold: #b88a3e;
    --gold-light: #e3b86a;
    --ink: #222222;
    --bronze: #7f5a26;
    --petal: #fdfaf5;
  }
  * { margin: 0; padding: 0; box-sizing: border-box; }
  html, body { width: 1200px; height: 888px; overflow: hidden; }
  body { background: var(--backdrop); position: relative; }

  .sign {
    position: absolute;
    left: 102px;
    width: 1001px;
    background: var(--frame-dark);
    box-shadow: 3px 5px 6px rgba(0,0,0,0.35);
    overflow: hidden;
  }
  .sign--wall { top: 88px; height: 529px; }
  .sign--strip { top: 703px; height: 108px; }

  .marble {
    position: absolute;
    background:
      radial-gradient(ellipse 12% 35% at 80% 45%, rgba(217,199,166,0.5), transparent 70%),
      radial-gradient(ellipse 30% 25% at 30% 70%, rgba(236,232,225,0.9), transparent 70%),
      linear-gradient(160deg, var(--marble-light), var(--marble-mid) 60%, var(--marble-light));
  }
  .sign--wall .marble { left: 16px; top: 15px; right: 14px; bottom: 15px; }
  .sign--strip .marble { left: 14px; top: 10px; right: 10px; bottom: 10px; }

  .gold-lines { position: absolute; inset: 0; width: 100%; height: 100%; }
  .gold-lines line, .gold-lines polyline { stroke: var(--gold); stroke-width: 2; fill: none; }

  .floral {
    position: absolute;
    border-radius: 50%;
    background: radial-gradient(closest-side, var(--petal) 0%, var(--petal) 45%, rgba(227,184,106,0.35) 75%, rgba(227,184,106,0) 100%);
  }

  .gold-text {
    background: linear-gradient(180deg, var(--gold-dark) 0%, var(--gold-light) 55%, var(--gold-dark) 100%);
    -webkit-background-clip: text;
    background-clip: text;
    color: transparent;
  }

  .welcome {
    position: absolute;
    left: 0; right: 0; top: 8px;
    text-align: center;
    font-family: "Dancing Script", cursive;
    font-weight: 700;
    font-size: 195px;
    line-height: 1.1;
    filter: drop-shadow(2px 3px 0 rgba(255,255,255,0.9));
  }
  .occasion {
    position: absolute;
    left: 0; right: 0; top: 226px;
    text-align: center;
    font-family: "Cinzel", serif;
    font-size: 68px;
    letter-spacing: 3px;
    color: var(--ink);
    white-space: nowrap;
  }
  .divider {
    position: absolute;
    left: 374px; top: 330px;
    width: 206px; height: 3px;
    background: linear-gradient(90deg, transparent, var(--gold) 20%, var(--gold-dark) 60%, transparent);
  }
  .couple {
    position: absolute;
    left: 0; right: 0; top: 360px;
    text-align: center;
    font-family: "Libre Baskerville", serif;
    font-weight: 700;
    font-size: 54px;
    color: var(--bronze);
    white-space: nowrap;
  }
  .date {
    position: absolute;
    left: 0; right: 0; top: 432px;
    text-align: center;
    font-family: "Cinzel", serif;
    font-size: 44px;
    color: var(--ink);
  }
  .strip-title {
    position: absolute;
    left: 150px; right: 45px; top: 8px;
    text-align: center;
    font-family: "Dancing Script", cursive;
    font-weight: 700;
    font-size: 66px;
    line-height: 1.2;
    white-space: nowrap;
  }
</style>
</head>
<body>

<section class="sign sign--wall" aria-label="Main wall welcome sign">
  <div class="marble" role="img" aria-label="White marble texture with gold veins"></div>
  <svg class="gold-lines" viewBox="0 0 1001 529" aria-hidden="true">
    <polyline points="22,10 990,55 975,520 12,480 22,10"/>
    <line x1="280" y1="2" x2="995" y2="30"/>
    <line x1="160" y1="486" x2="720" y2="527"/>
  </svg>
  <div class="floral" style="left:22px;top:4px;width:120px;height:140px;" role="img" aria-label="Small gold-outlined flower bud with leaves"></div>
  <div class="floral" style="left:850px;top:-10px;width:165px;height:215px;" role="img" aria-label="Gold-outlined white lilies"></div>
  <div class="floral" style="left:-30px;top:310px;width:260px;height:250px;" role="img" aria-label="Large gold-outlined white lily with leaves"></div>
  <div class="floral" style="left:700px;top:355px;width:320px;height:200px;" role="img" aria-label="Cluster of gold-outlined white lilies"></div>

  <h1 class="welcome gold-text">Welcome</h1>
  <p class="occasion">TO OUR WEDDING</p>
  <div class="divider"></div>
  <p class="couple">Helena &amp; Marcus</p>
  <p class="date">21.10.2021</p>
</section>

<section class="sign sign--strip" aria-label="Long wall welcome banner">
  <div class="marble" role="img" aria-label="White marble texture"></div>
  <svg class="gold-lines" viewBox="0 0 1001 108" aria-hidden="true">
    <polyline points="20,12 985,10 990,98 14,100 20,12"/>
    <line x1="120" y1="4" x2="900" y2="16"/>
  </svg>
  <div class="floral" style="left:-10px;top:-10px;width:240px;height:128px;" role="img" aria-label="Gold-outlined white lilies"></div>
  <div class="floral" style="left:865px;top:-10px;width:140px;height:128px;" role="img" aria-label="Gold-outlined white lily"></div>

  <p class="strip-title gold-text">Welcome To Our Wedding</p>
</section>

</body>
</html>
```